tolv Marketing Brochure for construction of multi-million dollar homes in the Caribbean

Design a marketing brochure for a construction company operating in the Caribbean for ultra high-end signature homes and villas. Target audience is ultra high net worth individuals, families, international property developers and hotel chains. We have provided an our marketing brochure for reference but would like a totally new look and feel with updated wording and photos (also provided). The company logo of light and dark blue circles and 'tolv' with the 's' in superscript must feature throughout. Further information can be extracted from the company's website: tolvharbour.example. Depending on how this goes there may be additional projects such as website and log redesign. Thanks!

Target Market(s)

Target audience is ultra high net worth individuals, families, international property developers and hotel chains.

Font styles to use
Other font styles liked:
• see logo for desired phones

Colors
3aa7d7
0655a3
85cae6
3176b5
85acd3
33a6d7
cee9f5
cedeed

Requirements
Must have
• Detailed company info including projects and employee profiles - must be bold, brilliant and eye-catching.
Nice to have
• Colour
Should not have
• Too much info.

```html
<!DOCTYPE html>
<html lang="en">
<head>
<meta charset="utf-8">
<title>tolv Caribbean – Company Profile Brochure</title>
<link rel="stylesheet" href="https://fonts.googleapis.com/css2?family=Montserrat:wght@400;600;700;800&family=Oswald:wght@300;600&family=Mulish:wght@400;600&display=swap">
<style>
  :root{
    --navy:#2c3895;
    --teal:#72c4d0;
    --sky:#3aa7d7;
    --deep:#0655a3;
    --ink:#3b3b3b;
    --paper:#ffffff;
    --stage-top:#9c9c9c;
    --stage-bottom:#8e8e8e;
    --rule:#b9b9b9;
  }
  *{box-sizing:border-box;margin:0;padding:0}
  html,body{width:956px;height:1200px;overflow:hidden}
  body{position:relative;font-family:"Montserrat",sans-serif;background:var(--stage-bottom)}
  .stage-top{position:absolute;left:0;top:0;width:956px;height:780px;background:var(--stage-top)}
  .page{position:absolute;background:var(--paper);overflow:hidden}
  .page > svg{position:absolute;left:0;top:0}
  .abs{position:absolute}

  .brand{display:flex;align-items:center;gap:4px;color:var(--navy);font-family:"Montserrat",sans-serif;font-weight:400;line-height:1}
  .brand-dot{border-radius:50%;background:var(--navy)}
  .tagline{font-family:"Montserrat",sans-serif;color:#555;letter-spacing:.2px}

  .section-label{position:absolute;color:#fff;font-family:"Mulish",sans-serif;font-weight:600}

  /* front cover */
  .front{left:40px;top:60px;width:470px;height:324px}
  .front .brand{right:30px;top:22px;font-size:30px}
  .front .brand-dot{width:22px;height:22px}
  .front .tagline{right:26px;top:56px;font-size:6px}
  .cover-title{left:34px;top:92px}
  .cover-title .t1{font-size:34px;font-weight:800;color:var(--navy);line-height:1}
  .cover-title .t2{font-size:44px;font-weight:800;color:var(--teal);line-height:.95}
  .cover-title .t3{font-size:9px;font-weight:600;color:var(--navy);margin-top:4px}
  .thanks{right:18px;top:254px;color:#fff;text-align:right}
  .thanks .big{font-family:"Oswald",sans-serif;font-weight:600;font-size:24px;line-height:1}
  .thanks .small{font-size:9px;line-height:1.2}

  /* back cover */
  .back{left:446px;top:410px;width:470px;height:324px}
  .back .brand{left:22px;top:68px;font-size:28px}
  .back .brand-dot{width:20px;height:20px}
  .back .tagline{left:110px;top:72px;font-size:6px}
  .copyright{right:40px;bottom:9px;font-family:"Mulish",sans-serif;font-size:8px;letter-spacing:1.4px;color:#555}

  /* inner pages */
  .inner1{left:40px;top:830px;width:438px;height:302px}
  .inner2{left:478px;top:830px;width:438px;height:302px}
  .inner-brand{right:16px;top:12px}
  .inner-brand .brand{font-size:12px}
  .inner-brand .brand-dot{width:8px;height:8px}
  .welcome{left:14px;top:60px;font-family:"Oswald",sans-serif;font-size:34px;line-height:1}
  .welcome .w1{color:var(--navy);font-weight:600}
  .welcome .w2{color:var(--teal);font-weight:300}
  .intro{left:225px;top:50px;width:200px}
  .intro h2{font-size:15.5px;font-weight:600;color:var(--teal);line-height:1.1}
  .intro h3{font-size:15.5px;font-weight:800;color:var(--navy);line-height:1.1;margin-bottom:8px}
  .copy{font-family:"Mulish",sans-serif;font-size:5.4px;line-height:1.62;color:var(--ink);text-align:justify}
  .col-right{left:246px;width:178px}
  .copy.on-navy{color:#fff}
</style>
</head>
<body>
<div class="stage-top"></div>

<!-- Front cover -->
<section class="page front" aria-label="Front cover">
  <svg width="470" height="324" viewBox="0 0 470 324">
    <defs>
      <linearGradient id="villaTop" x1="0" y1="0" x2="1" y2="1">
        <stop offset="0" stop-color="#5c7a3c"/><stop offset=".55" stop-color="#8a8a7e"/><stop offset="1" stop-color="#4d6d33"/>
      </linearGradient>
      <linearGradient id="villaEntry" x1="0" y1="0" x2="1" y2="1">
        <stop offset="0" stop-color="#6aa0c8"/><stop offset=".4" stop-color="#b5773f"/><stop offset="1" stop-color="#3f6d2c"/>
      </linearGradient>
    </defs>
    <polygon points="315,70 470,70 470,232 342,232 292,150" fill="url(#villaTop)" role="img" aria-label="Aerial photo of a hillside villa with an infinity pool"/>
    <polygon points="0,192 258,180 300,252 262,324 0,324" fill="url(#villaEntry)" role="img" aria-label="Photo of a timber villa entrance framed by palm trees"/>
    <polygon points="318,244 470,244 470,324 290,324" fill="var(--navy)"/>
    <line x1="262" y1="168" x2="286" y2="98" stroke="var(--teal)" stroke-width="2.5"/>
    <line x1="274" y1="176" x2="296" y2="118" stroke="var(--navy)" stroke-width="2.5"/>
    <line x1="316" y1="310" x2="328" y2="274" stroke="#fff" stroke-width="1.5"/>
    <line x1="324" y1="310" x2="336" y2="274" stroke="#fff" stroke-width="1.5"/>
  </svg>
  <div class="abs brand"><span class="brand-dot"></span>tolv</div>
  <div class="abs tagline">engineering . management . construction</div>
  <div class="abs cover-title">
    <div class="t1">COMPANY</div>
    <div class="t2">PROFILE</div>
    <div class="t3">Welcome to tolv, professionals in building</div>
  </div>
  <div class="abs thanks">
    <div class="big">THANK YOU</div>
    <div class="small">For your interest in<br>tolv Caribbean Ltd.</div>
  </div>
</section>

<!-- Back cover -->
<section class="page back" aria-label="Back cover">
  <svg width="470" height="324" viewBox="0 0 470 324">
    <defs>
      <linearGradient id="coast" x1="0" y1="0" x2="0" y2="1">
        <stop offset="0" stop-color="#2458b8"/><stop offset=".3" stop-color="#6ea2dc"/>
        <stop offset=".42" stop-color="#a48c6a"/><stop offset=".62" stop-color="#7d7a55"/>
        <stop offset=".7" stop-color="#1f5aa0"/><stop offset="1" stop-color="#0d3d7a"/>
      </linearGradient>
    </defs>
    <rect x="0" y="0" width="452" height="294" fill="url(#coast)" role="img" aria-label="Photo of a rocky Caribbean headland with villas above a deep blue sea"/>
    <rect x="452" y="0" width="18" height="294" fill="#c9d2de"/>
    <polygon points="0,50 300,24 270,96 0,118" fill="var(--paper)"/>
    <line x1="282" y1="112" x2="302" y2="60" stroke="#fff" stroke-width="2"/>
    <line x1="292" y1="112" x2="312" y2="60" stroke="#fff" stroke-width="2"/>
  </svg>
  <div class="abs brand"><span class="brand-dot"></span>tolv</div>
  <div class="abs tagline">engineering . management . construction</div>
  <div class="abs copyright">Copyright © tolv Caribbean 2018. All Rights Reserved.</div>
</section>

<div class="section-label" style="left:58px;top:682px;font-size:27px">Brochure Front &amp; Back</div>

<!-- Inner 1 -->
<section class="page inner1" aria-label="Inner page 1">
  <svg width="438" height="302" viewBox="0 0 438 302">
    <defs>
      <linearGradient id="terrace" x1="0" y1="0" x2="1" y2="1">
        <stop offset="0" stop-color="#6b4a2e"/><stop offset=".5" stop-color="#5f9ab8"/><stop offset="1" stop-color="#9c8a6a"/>
      </linearGradient>
      <linearGradient id="poolView" x1="0" y1="0" x2="1" y2="0">
        <stop offset="0" stop-color="#c8c6c0"/><stop offset=".6" stop-color="#3ba6c9"/><stop offset="1" stop-color="#6fa04e"/>
      </linearGradient>
      <linearGradient id="estate" x1="0" y1="0" x2="1" y2="1">
        <stop offset="0" stop-color="#4f7a35"/><stop offset=".5" stop-color="#9a9486"/><stop offset="1" stop-color="#3c6a2a"/>
      </linearGradient>
    </defs>
    <line x1="0" y1="22" x2="312" y2="22" stroke="var(--navy)" stroke-width="1"/>
    <polygon points="0,150 170,150 196,200 170,250 0,250" fill="url(#terrace)" role="img" aria-label="Photo of an open-air terrace lounge overlooking the sea"/>
    <polygon points="0,256 190,256 210,302 0,302" fill="url(#poolView)" role="img" aria-label="Photo of an infinity pool facing a white sand bay"/>
    <polygon points="218,202 438,202 438,302 180,302 196,252" fill="url(#estate)" role="img" aria-label="Aerial photo of a large villa estate among palms"/>
    <line x1="156" y1="130" x2="194" y2="170" stroke="var(--navy)" stroke-width="1.2"/>
    <line x1="166" y1="130" x2="210" y2="176" stroke="var(--teal)" stroke-width="1.2"/>
  </svg>
  <div class="abs inner-brand"><div class="brand"><span class="brand-dot"></span>tolv</div></div>
  <div class="abs welcome"><span class="w1">WELCOME</span> <span class="w2">TO</span></div>
  <div class="abs intro">
    <h2>TOLV PROFESSIONALS</h2>
    <h3>IN BUILDING</h3>
    <p class="copy">If you are looking to build your ultimate dream home in your own piece of paradise, tolv Caribbean Ltd ("tolv") can not only make it a reality, but can do it in a way that is seamless and specifically tailored for you and your needs. tolv covers all aspects of the building process, from conceptual project planning and design, through to completion and everything in between. Specialising in creating luxurious private residences throughout the Caribbean, tolv has built an enviable portfolio of breathtaking villas and opulent homes for extremely satisfied clientele.</p>
  </div>
</section>

<!-- Inner 2 -->
<section class="page inner2" aria-label="Inner page 2">
  <svg width="438" height="302" viewBox="0 0 438 302">
    <defs>
      <linearGradient id="bath" x1="0" y1="0" x2="0" y2="1">
        <stop offset="0" stop-color="#cbbfa3"/><stop offset=".5" stop-color="#e2ddd2"/><stop offset="1" stop-color="#f1efea"/>
      </linearGradient>
    </defs>
    <line x1="0" y1="22" x2="322" y2="22" stroke="var(--navy)" stroke-width="1"/>
    <rect x="14" y="198" width="424" height="104" fill="var(--navy)"/>
    <rect x="14" y="44" width="190" height="248" fill="#9a9a9a"/>
    <rect x="16" y="46" width="186" height="244" fill="url(#bath)" role="img" aria-label="Photo of a marble bathroom vanity with brass taps and orchids"/>
    <polyline points="204,88 226,88 226,150" fill="none" stroke="var(--rule)" stroke-width="0.8"/>
  </svg>
  <div class="abs inner-brand"><div class="brand"><span class="brand-dot"></span>tolv</div></div>
  <p class="abs copy col-right" style="top:66px">tolv caters to clients who are not able to be present for the duration of their project and therefore require building professionals to represent their best interests. From the beginning of the process, our services will help you understand in detail how we get to the end product with the agreed original parameters.</p>
  <p class="abs copy col-right" style="top:126px">Our team consists largely of British and American personnel with support from local communities and consists of Project Managers, Chartered Builders, Civil and Structural Engineers, Chartered Quantity Surveyors, Estimators and Qualified Electrical &amp; Mechanical Engineers.</p>
  <p class="abs copy col-right on-navy" style="top:212px">tolv have an unparalleled network of professional service providers available for any nature of high-end development, having partnered with a diverse range of premium project design teams, architects, engineers and specialist trade contractors. Due to these long and established relationship, tolv is able to provide clients the greatest choice of resources, mobilise at short notice and ensure superior client delivery every time.</p>
</section>

<div class="section-label" style="left:222px;top:1150px;font-size:15px">INNER 1</div>
<div class="section-label" style="left:660px;top:1150px;font-size:15px">INNER 2</div>
</body>
</html>
```